Corvella Website Homepage

Committed to delivering quality content, quillpagewords.com is a content providing company. Equipped with resourceful writers with industry experience, we promise to empower our clients with content that is tailor-made to address specific requirements of their target Audience.

We need a website home page and one internal page designed. It is very important that the page be laid out with SEO in mind. We like the idea of using five images as navigation to our services. The five major services we offer are:
• Web Content writing (articles, features, website copy etc)
• Business Content writing (Press release, mailers & flyers, brochure/catalog)
• Personal Content writing (blog, speech writing)
• Hire a writer/editor
• Proof reading and editing services
The sample template (http://pv7.layoutdemo-hub.net/dx_48270/index.html) included has five images in the first fold. Designer can choose the right image for each service and lay over the service name on the image. Please do not use flash ( We will use javascripts). We need to have a detailed right side nav as in the template for SEO reasons. There will be some marketing ad- copy below the main images. Followed by a 200 character SEO optimized text defining our services in further detail. Apart from these a designer is free to use his creativity. The name of the site will be http://www.quillpagewords.com/. This name will need a logo too. Please include it as part of design. Corvellacorp is the owner of quillpagewords.com. We already have a logo for Corvella that is attached here as a separate file.

We have some taglines that need to be incorporated in the home page and other pages.
Please provide link button for Home, About us, Services, Samples, Pricing, Clients, Career, Contact us.

Links can be given on TOP, Sideways and Bottom and in the drop down menu of services etc.

Reason: Hi

We have made our project guaranteed and extended deadline by 5 days so you get more time to complete our project.

Thanks and Regards,

Ravindra Kulkarni
Corvellacorp

Target Market(s)

Product Marketing Companies - Mostly in US.
Media companies which publish articles on various subjects. Travel and Lifestyle related sites, Educational Websites, Government Websites, Health related websites,

Industry/Entity Type

Marketing

Requirements
Must have
• Color of Homepage should blend with sober mood of the content. Writing Services should get highlighted in such a way that any person serious about the business visiting the site get attracted to read on the details of our content services. Most space should be used for details of writing services and links for our various pages and services. Webpage should be downloaded in lowest possible time.
Nice to have
• We have some idea about the website layouts;-http://www.skinbazaarly.net/site-layouts/48270.html - layout of information http://www.skinbazaarly.net/site-layouts/47359.html - for kind of marketing http://pv7.layoutdemo-hub.net/dx_48615/index.html - for colors
we attach a word file representing our idea in some way but not limited to it.
Should not have
• Gaudy (aggressive dark) colors. It should not be cluttered. No flash.

```html
<!DOCTYPE html>
<html lang="en">
<head>
<meta charset="utf-8">
<title>About Us – Quillpage Words</title>
<link href="https://fonts.googleapis.com/css2?family=Arimo:wght@400;700&family=Gelasio:wght@400&display=swap" rel="stylesheet">
<style>
:root{
  --cyan:#0fb8e6;
  --blue:#2e8bbd;
  --link:#0a8fcf;
  --red:#c8101b;
  --maroon:#8a0d18;
  --text:#333;
  --rule:#c9c9c9;
  --band:#f2f0f0;
  --white:#fff;
}
*{box-sizing:border-box;margin:0;padding:0}
html,body{width:1097px;height:1200px;overflow:hidden;background:var(--white)}
body{position:relative;font-family:"Arimo",Arial,sans-serif;color:var(--text)}
a{text-decoration:none;color:inherit}
.abs{position:absolute}
.topbar{left:0;top:0;width:1097px;height:7px;background:var(--cyan)}
.brand{left:137px;top:26px}
.brand-name{font-size:40px;color:var(--blue);letter-spacing:1px;line-height:1}
.brand-sub{font-size:21px;color:var(--blue);letter-spacing:3px;margin-top:4px}
.phone{right:137px;top:24px;display:flex;align-items:center;gap:8px;font-size:14px;color:#444}
.phone b{color:#111}
.nav{left:380px;top:83px;display:flex;font-size:14px;color:#333}
.nav a{padding:0 13px;border-right:1px dotted #bbb;line-height:22px}
.nav a:last-child{border-right:0;padding-right:0}
.nav a.active{color:var(--red)}
.banner{left:137px;top:120px;width:823px;height:129px;background:var(--blue);box-shadow:0 8px 6px -6px rgba(0,0,0,.35)}
.banner h1{position:absolute;left:19px;top:76px;font-family:"Gelasio",Georgia,serif;font-weight:400;font-size:27px;color:#fff}
.banner-photo{position:absolute;right:0;top:0;width:274px;height:129px;background:linear-gradient(120deg,#d9cbbd,#f1ede8 55%,#c9d3dc)}
.crumb{left:137px;top:274px;width:523px;border-top:1px dotted var(--rule);border-bottom:1px dotted var(--rule);padding:7px 0;font-size:11px}
.crumb a{color:var(--link)}
.crumb b{color:#333}
.intro{left:137px;top:313px;width:523px;font-size:10.4px;line-height:17.1px;color:#333}
.tiles{left:137px;top:437px;width:155px;height:320px;background:linear-gradient(180deg,#f4f4f4,#eee)}
.feature{left:313px;top:433px;width:352px}
.feature h2{font-family:"Gelasio",Georgia,serif;font-weight:400;font-size:16px;color:var(--link);margin-bottom:10px}
.feature p{font-size:10.2px;line-height:17.1px;margin-bottom:17px}
.why{left:686px;top:274px;width:274px;height:436px;border:1px solid #e2e2e2;background:#fff}
.why-head{position:absolute;left:-5px;top:12px;width:284px;height:62px;background:linear-gradient(180deg,#9c0f1c,var(--maroon));color:#fff;font-family:"Gelasio",Georgia,serif;font-size:15px;line-height:19px;padding:12px 0 0 20px}
.why-list{position:absolute;left:13px;top:88px;width:248px;list-style:none}
.why-list li{display:flex;align-items:center;gap:8px;border-bottom:1px dotted var(--rule);font-size:12.5px;color:#222}
.why-list li:last-child{border-bottom:0}
.why-list b{color:var(--red)}
.ico{width:36px;height:34px;flex:none;border-radius:4px}
.band{left:0;top:806px;width:1097px;height:244px;background:var(--band);border-top:1px solid #ddd}
.col{top:820px;width:258px}
.col h3{font-family:"Gelasio",Georgia,serif;font-weight:400;font-size:16px;color:#333;display:flex;align-items:center;gap:8px;padding-bottom:10px;border-bottom:1px dotted var(--rule)}
.col ul{list-style:none;margin-top:8px}
.col li{font-size:11px;line-height:27.4px;color:var(--link)}
.col li::before{content:"→";color:#333;margin:0 4px}
.col .quote{font-size:10.4px;line-height:17.1px;margin-top:9px;color:#333}
.col .by{font-size:10.5px;font-weight:700;margin-top:10px}
.more{font-size:11px;color:var(--link);border-top:1px dotted var(--rule);padding-top:10px;width:258px}
.field{width:257px;height:28px;border:1px solid #ddd;border-radius:14px;background:#fff;font-size:11px;padding:8px 14px;color:#222}
.subscribe{position:absolute;right:0;top:0;width:88px;height:28px;border-radius:0 14px 14px 0;background:var(--blue);color:#fff;font-family:"Gelasio",Georgia,serif;font-size:16px;text-align:center;line-height:28px}
.social{display:flex;align-items:center;gap:6px;border-top:1px dotted var(--rule);border-bottom:1px dotted var(--rule);padding:12px 0;margin-top:12px;font-family:"Gelasio",Georgia,serif;font-size:16px}
.social span{margin-right:16px}
.dot{width:45px;height:45px;border-radius:50%}
.lined{left:0;top:1050px;width:1097px;height:150px;background:repeating-linear-gradient(180deg,#fff 0 11px,#e7eef7 11px 12px)}
.foot-nav{left:137px;top:1104px;display:flex;gap:18px;font-size:10.5px;color:#444;letter-spacing:.5px}
.foot-nav .cur{color:#111}
.copy{left:137px;top:1131px;font-size:9.5px;color:#444}
.owner{right:137px;top:1096px;text-align:right}
.owner-name{display:flex;align-items:center;justify-content:flex-end;gap:8px;font-size:28px;color:var(--red)}
.owner-name i{width:16px;height:16px;background:var(--red);display:block}
.owner p{font-size:10px;color:#333;margin-top:12px;letter-spacing:.3px}
</style>
</head>
<body>
<div class="abs topbar"></div>

<a class="abs brand" href="#">
  <div class="brand-name">QUILLPAGE</div>
  <div class="brand-sub">WORDS</div>
</a>

<div class="abs phone">
  <svg width="24" height="24" viewBox="0 0 24 24"><rect width="24" height="24" rx="4" fill="#333"/><path d="M8 5c-1 1-2 2-1 5s4 7 7 8 4 0 5-1l-2-3-2 1c-2-1-4-3-5-5l1-2z" fill="#fff"/></svg>
  <span>Call Us: <b>123 456 789</b></span>
</div>

<nav class="abs nav">
  <a href="#">home</a><a href="#" class="active">about us</a><a href="#">services ▾</a><a href="#">samples</a><a href="#">pricing</a><a href="#">clients</a><a href="#">career</a><a href="#">contact us</a>
</nav>

<header class="abs banner">
  <h1>About Us...</h1>
  <div class="banner-photo" role="img" aria-label="Smiling businesswoman with colleagues in an office"></div>
</header>

<div class="abs crumb"><a href="#">Home</a> &nbsp;»&nbsp; <b>About Us</b></div>

<p class="abs intro">Lorem Ipsum is simply dummy text of the printing and typesetting industry. Lorem Ipsum has been the industry's standard dummy text ever since the 1500s, when an unknown printer took a galley of type and scrambled it to make a type specimen book. It has survived not only five centuries, but also the leap into electronic typesetting, remaining essentially unchanged. It was popularised in the 1960s with the release of Typemark sheets containing Lorem Ipsum passages, and more recently with desktop publishing software like Pressline Layout including versions of Lorem Ipsum.</p>

<div class="abs tiles" role="img" aria-label="Crossword grid of red and blue letter tiles spelling writing qualities"></div>

<section class="abs feature">
  <h2>It is a long established fact that a reader</h2>
  <p>It is a long established fact that a reader will be distracted by the readable content of a page when looking at its layout. The point of using Lorem Ipsum is that it has a more-or-less normal distribution of letters, as opposed to using 'Content here, content here', making it look like readable English.</p>
  <p>Many desktop publishing packages and web page editors now use Lorem Ipsum as their default model text, and a search for 'lorem ipsum' will uncover many web sites still in their infancy. Various versions have evolved over the years, sometimes by accident, sometimes on purpose (injected humour and the like).</p>
  <p>There are many variations of passages of Lorem Ipsum available, but the majority have suffered alteration in some form, by injected humour, or randomised words which don't look even slightly believable.</p>
  <p>If you are going to use a passage of Lorem Ipsum, you need to be sure there isn't anything embarrassing hidden in the middle of text.</p>
</section>

<aside class="abs why">
  <div class="why-head">Why choose Quillpagewords.com<br>to “e - SOURCE” your content</div>
  <ul class="why-list">
    <li style="height:53px"><span class="ico" style="background:#b8c4de" role="img" aria-label="Language flags icon"></span><span><b>E</b>NGLISH American and British.</span></li>
    <li style="height:53px"><span class="ico" style="background:#9fd3ef" role="img" aria-label="Growth chart icon"></span><span><b>S</b>UCCESS stories of our clients</span></li>
    <li style="height:47px"><span class="ico" style="background:#c9dcea" role="img" aria-label="Magnifying glass icon"></span><span><b>O</b>PTIMIZED content for Search Engines</span></li>
    <li style="height:48px"><span class="ico" style="background:#d7a3a8" role="img" aria-label="Shopping cart icon"></span><span><b>U</b>LTRA &nbsp;high speed delivery</span></li>
    <li style="height:47px"><span class="ico" style="background:#9db8d6" role="img" aria-label="Book icon"></span><span>Intensive <b>R</b>ESEARCH</span></li>
    <li style="height:51px"><span class="ico" style="background:#8ec8e6" role="img" aria-label="Dollar sign icon"></span><span>Competitive <b>C</b>OST</span></li>
    <li style="height:53px"><span class="ico" style="background:#bdbfae" role="img" aria-label="Team icon"></span><span>Team of subject matter <b>E</b>XPERTS</span></li>
  </ul>
</aside>

<div class="abs band"></div>

<section class="abs col" style="left:137px">
  <h3><svg width="22" height="22" viewBox="0 0 22 22"><path d="M3 19l3-8 9-9 5 5-9 9z" fill="#a31522"/><path d="M3 19l4-4" stroke="#333" stroke-width="1.5"/></svg>The Five Major Services</h3>
  <ul>
    <li>Web Content writing</li>
    <li>Business Content writing</li>
    <li>Personal Content writing</li>
    <li>Hire a writer/editor</li>
    <li>Proof reading and editing services</li>
  </ul>
  <div class="more" style="margin-top:7px">Read More...</div>
</section>

<section class="abs col" style="left:420px">
  <h3><svg width="32" height="22" viewBox="0 0 32 22"><ellipse cx="11" cy="8" rx="10" ry="6" fill="#a31522"/><ellipse cx="22" cy="13" rx="9" ry="6" fill="#1aaee6"/></svg>Clients Speak</h3>
  <p class="quote">It is a long established fact that a reader will be distracted by the readable content of a page when looking at its layout. The point of using Lorem Ipsum is that it has a more-or-less normal distribution of letters, as opposed to using 'Content here, content here', making it look like readable English.</p>
  <p class="by">— John Smith, A.B.C. Corp</p>
  <div class="more" style="margin-top:17px">Read More...</div>
</section>

<section class="abs col" style="left:702px">
  <h3><svg width="28" height="22" viewBox="0 0 28 22"><rect x="1" y="5" width="26" height="16" fill="#a31522"/><path d="M1 5l13 9 13-9" fill="none" stroke="#fff" stroke-width="1.5"/></svg>Subscribe Our Newsletter</h3>
  <div class="field" style="margin-top:11px">Your Name</div>
  <div class="field" style="position:relative;margin-top:4px">Your Email Address<span class="subscribe">Subscribe</span></div>
  <div class="social"><span>Social Network...</span><i class="dot" style="background:#1ab8ea"></i><i class="dot" style="background:#1760a8"></i></div>
</section>

<div class="abs lined"></div>
<nav class="abs foot-nav">
  <a href="#">home</a><a href="#">about us</a><a href="#">services</a><a href="#">samples</a><a href="#" class="cur">pricing</a><a href="#">clients</a><a href="#">career</a><a href="#">contact us</a>
</nav>
<p class="abs copy">Copyright © 2011 <b>Quillpage Words</b>. &nbsp;| &nbsp;All Rights Reserved.</p>
<div class="abs owner">
  <div class="owner-name"><i></i>CORVELLA</div>
  <p>Corvellacorp is the owner of quillpagewords.com</p>
</div>
</body>
</html>
```